A start up special flyer design!

Hi All - Have updated the attachment content - This is the info required for the designs.
I need a catchy flyer to send out to a few areas to advertise the start of my plumbing business!
The flyer will contain an offer for customers, which will need to have some key details on it. See attached. Feel free to fit these criteria into the flyer given your knowledge on design and messaging principles. Key thing to get across to customers is the discount and special offer, and that it is a start up offer.
I have a logo that needs to be on the flyer as well - let me know what format you require and I will send through to you.
The color scheme needs to be blue / grey / black / white.
Let me know if you have any questions.
I

```html
<!DOCTYPE html>
<html lang="en">
<head>
<meta charset="utf-8">
<title>Marlowpipe Plumbing – Start-up Offer Flyer</title>
<link rel="stylesheet" href="https://fonts.googleapis.com/css2?family=Roboto+Condensed:wght@700&family=Open+Sans:wght@400;600;700&display=swap">
<style>
  :root{
    --blue:#1c9be8;
    --blue-deep:#0f86d6;
    --cyan:#1fc6ee;
    --dark:#25282b;
    --ink:#2a2d30;
    --white:#ffffff;
    --silver-1:#ffffff;
    --silver-2:#dcdfe2;
    --page:#eceded;
    --paper-1:#f7f8f9;
    --paper-2:#e3e6e9;
  }
  *{margin:0;padding:0;box-sizing:border-box}
  html,body{width:825px;height:1200px;overflow:hidden}
  body{background:var(--page);position:relative;font-family:"Open Sans",Arial,sans-serif}

  .flyer{position:absolute;left:107px;top:168px;width:611px;height:865px;overflow:hidden;
    background:linear-gradient(180deg,var(--paper-1) 0%,var(--paper-2) 70%,#d9dde1 100%)}
  .flyer-shapes{position:absolute;inset:0;width:611px;height:865px}

  .headline{position:absolute;left:36px;top:28px;width:260px;font-family:"Roboto Condensed",Arial,sans-serif;
    font-weight:700;font-size:27px;line-height:31px;letter-spacing:-.3px;text-align:center}
  .headline .line-light{color:var(--white);display:block}
  .headline .line-dark{color:var(--dark);display:block}

  .brand{position:absolute;left:0;top:126px;width:320px;text-align:center;font-family:"Roboto Condensed",Arial,sans-serif;font-weight:700}
  .brand-name{display:block;color:var(--dark);font-size:35px;line-height:38px;letter-spacing:.3px}
  .brand-trade{display:block;color:var(--blue);font-size:54px;line-height:56px;letter-spacing:.5px}

  .offer{position:absolute;left:27px;top:280px;width:283px;text-align:center;font-family:"Roboto Condensed",Arial,sans-serif;font-weight:700}
  .offer-amount{display:block;color:var(--cyan);font-size:66px;line-height:70px}
  .offer-sub{display:block;color:var(--white);font-size:29px;line-height:32px;margin-top:2px}

  .terms{position:absolute;right:32px;top:349px;width:260px;list-style:none;text-align:right;font-size:13px;line-height:17.5px;color:var(--ink)}
  .terms li{position:relative;padding-right:22px}
  .terms li::after{content:"";position:absolute;right:0;top:4px;width:9px;height:9px;border-radius:50%;background:var(--cyan)}

  .pill{position:absolute;left:48px;height:37px;border-radius:0 18px 18px 0;border:1px solid var(--dark);
    color:var(--white);font-weight:600;font-size:17px;line-height:35px;padding-left:14px;
    box-shadow:0 10px 14px -8px rgba(0,0,0,.25)}
  .pill-gst{top:468px;width:478px;background:var(--cyan)}
  .pill-check{top:535px;width:525px;background:var(--blue)}
  .pill-features{top:598px;width:467px;background:var(--cyan);color:var(--dark);font-size:15.5px;display:flex;align-items:center;padding-left:20px}
  .feature{display:flex;align-items:center;margin-right:16px}
  .feature svg{margin-right:10px}

  .gallery-item{position:absolute;top:662px;width:150px;height:150px;border-radius:50%;
    background:conic-gradient(var(--cyan) 0 70%,var(--blue-deep) 70% 100%);}
  .gallery-item::before{content:"";position:absolute;inset:10px;border-radius:50%;background:var(--dark)}
  .gallery-photo{position:absolute;inset:15px;border-radius:50%;z-index:1}
  .gallery-1{left:40px}.gallery-2{left:228px}.gallery-3{left:415px}
  .gallery-1 .gallery-photo{background:radial-gradient(circle at 40% 40%,#e9eef2,#8fa7bf 60%,#2f4f7a)}
  .gallery-2 .gallery-photo{background:radial-gradient(circle at 50% 45%,#f4f1ed,#c9b8a8 55%,#4b6a9a)}
  .gallery-3 .gallery-photo{background:radial-gradient(circle at 55% 50%,#f1f3f5,#b9c1c8 55%,#7b8790)}

  .hero-photo{position:absolute;left:0;top:0;width:611px;height:290px;
    clip-path:polygon(304px 0,611px 0,611px 288px,344px 288px);
    background:linear-gradient(135deg,#f2f4f6 0%,#d7dde3 35%,#7d8fa8 60%,#2f4d7c 85%,#1f2a38 100%)}

  .footer{position:absolute;left:0;top:812px;width:611px;height:53px;background:var(--dark);color:var(--white);
    font-size:11.5px;font-weight:700;text-align:center;line-height:53px;letter-spacing:-.1px}
  .footer .label{color:var(--cyan)}
  .footer .sep{margin:0 3px}
</style>
</head>
<body>
<main class="flyer">
  <svg class="flyer-shapes" viewBox="0 0 611 865" aria-hidden="true">
    <defs>
      <linearGradient id="silver" x1="0" y1="0" x2="0" y2="1">
        <stop offset="0" stop-color="#ffffff"/>
        <stop offset="1" stop-color="#d7dadd"/>
      </linearGradient>
      <linearGradient id="topBlue" x1="0" y1="0" x2="1" y2="1">
        <stop offset="0" stop-color="#2bb2f0"/>
        <stop offset="1" stop-color="#0f8ad9"/>
      </linearGradient>
    </defs>
    <!-- blue header block -->
    <polygon points="0,0 298,0 336,300 0,300" fill="url(#topBlue)"/>
    <!-- silver name band -->
    <polygon points="0,114 313,114 328,232 0,232" fill="url(#silver)"/>
    <!-- dark frame around hero photo -->
    <polygon points="290,0 306,0 346,284 611,284 611,330 330,300" fill="var(--dark)"/>
    <!-- cyan diagonal accent -->
    <polygon points="0,370 611,318 611,330 0,384" fill="var(--cyan)"/>
    <polygon points="0,384 611,330 611,334 0,388" fill="#ffffff" opacity=".7"/>
    <!-- offer banner -->
    <polygon points="27,264 310,264 310,402 168,428 27,402" fill="var(--cyan)"/>
    <polygon points="27,264 310,264 310,394 168,420 27,394" fill="var(--dark)"/>
    <!-- footer blue stripe -->
    <rect x="0" y="802" width="611" height="10" fill="var(--blue)"/>
  </svg>

  <div class="hero-photo" role="img" aria-label="Photo of a smiling plumber fixing pipes under a sink with a red wrench"></div>

  <h1 class="headline">
    <span class="line-light">All plumbing, draining</span>
    <span class="line-dark">and gasfitting works</span>
  </h1>

  <p class="brand">
    <span class="brand-name">MARLOWPIPE</span>
    <span class="brand-trade">PLUMBING</span>
  </p>

  <p class="offer">
    <span class="offer-amount">15% OFF</span>
    <span class="offer-sub">YOUR OVERALL BILL</span>
  </p>

  <ul class="terms">
    <li>Offer valid between 15 August 2016 to 15 October 2016</li>
    <li>Valid until 30 September 2016</li>
    <li>Quote valid for 12 months from the quote date</li>
  </ul>

  <p class="pill pill-gst">No GST payable, saving you additional 10% on your bill</p>
  <p class="pill pill-check">Plus, a free hot water health check and replacement quote</p>
  <div class="pill pill-features">
    <span class="feature">
      <svg width="20" height="26" viewBox="0 0 20 26" aria-hidden="true">
        <path d="M10 1C5 1 1.5 4.6 1.5 9.3 1.5 15.5 10 24 10 24s8.5-8.5 8.5-14.7C18.5 4.6 15 1 10 1z" fill="#fff"/>
        <circle cx="10" cy="9.3" r="3.4" fill="var(--cyan)"/>
      </svg>
      Local plumber
    </span>
    <span class="feature">
      <svg width="24" height="24" viewBox="0 0 24 24" aria-hidden="true">
        <rect x="1" y="10" width="5" height="12" rx="1" fill="#fff"/>
        <path d="M8 10.5 12.5 3c1.5-.5 2.8.6 2.4 2.2L14 9h6.2c1.3 0 2.2 1.2 1.9 2.4l-2 8.6c-.3 1.1-1.2 1.8-2.3 1.8H8z" fill="#fff"/>
      </svg>
      Quality work at a decent price
    </span>
  </div>

  <div class="gallery-item gallery-1"><div class="gallery-photo" role="img" aria-label="Photo of a plumber in a cap working beneath a sink"></div></div>
  <div class="gallery-item gallery-2"><div class="gallery-photo" role="img" aria-label="Photo of a plumber fitting pipework at a basin"></div></div>
  <div class="gallery-item gallery-3"><div class="gallery-photo" role="img" aria-label="Photo of hands tightening a chrome mixer tap with a wrench"></div></div>

  <footer class="footer">
    <span class="label">Ph:</span> 0400 123 456<span class="sep">|</span><span class="label">Email:</span> hello@marlowpipeplumbing.co<span class="sep">|</span><span class="label">Web:</span> www.marlowpipeplumbing.com
  </footer>
</main>
</body>
</html>
```